Ruler design for Brodmere Liquid waste

We require a very professional design for our marketing product 'Ruler'.
It will be on a white plastic ruler 315mm long and 39mm high.
0 – 30 on the top (in mm).
0 – 12 on the bottom (in inches).
Numbering in black (to be included as an example only) as it is already printed on the plastic stock.
I want logo, phone number, email and website.
Phone number - 08 8317 4925, email info@bwx.com.au, web www.brodmereliquidwaste.com
Large text - Your Local Grease Trap and Liquid Waste Specialists
Please stick to our colours.
Total workable text area –
Length 312mm
Height 24mm
You must supply Print ready pdf files with
all fonts embedded.
Please include crop marks plus 3mm bleed all round.
Marketing

```html
<!DOCTYPE html>
<html lang="en">
<head>
<meta charset="utf-8">
<title>Brodmere Liquid Waste – Ruler</title>
<link href="https://fonts.googleapis.com/css2?family=Oswald:wght@500&family=Open+Sans:wght@400;600&display=swap" rel="stylesheet">
<style>
  :root {
    --backdrop: #e9e6e2;
    --ruler-white: #ffffff;
    --brand-navy: #0f0f5e;
    --brand-orange: #f26a1b;
    --icon-yellow: #f2d416;
    --scale-ink: #1a1a1a;
    --text-white: #ffffff;
  }
  html, body {
    margin: 0;
    width: 1200px;
    height: 900px;
    overflow: hidden;
    background: var(--backdrop);
  }
  .canvas {
    position: relative;
    width: 1200px;
    height: 900px;
  }
  .ruler {
    position: absolute;
    left: 40px;
    top: 380px;
    width: 1120px;
    height: 139px;
    box-shadow: 0 6px 18px rgba(0,0,0,0.18);
  }
  .ruler-body { fill: var(--ruler-white); }
  .brand-band { fill: var(--brand-navy); }
  .tick { stroke: var(--scale-ink); stroke-width: 0.8; }
  .scale-number {
    font-family: "Open Sans", Arial, sans-serif;
    font-size: 10px;
    fill: var(--scale-ink);
  }
  .scale-number--inch { font-size: 13px; }
  .brand-mark { fill: var(--brand-orange); }
  .brand-name {
    font-family: "Oswald", "Arial Narrow", sans-serif;
    font-weight: 500;
    fill: var(--text-white);
    letter-spacing: 1px;
  }
  .contact-icon { fill: var(--icon-yellow); }
  .contact-icon-line { stroke: var(--brand-navy); stroke-width: 0.8; fill: none; }
  .contact-text {
    font-family: "Open Sans", Arial, sans-serif;
    font-size: 12px;
    fill: var(--text-white);
  }
  .headline {
    font-family: "Oswald", "Arial Narrow", sans-serif;
    font-weight: 500;
    font-size: 34px;
    fill: var(--brand-orange);
  }
</style>
</head>
<body>
<div class="canvas">
  <svg class="ruler" viewBox="0 0 1120 139" xmlns="http://www.w3.org/2000/svg">
    <defs>
      <pattern id="mm-scale" x="20" y="0" width="35" height="30" patternUnits="userSpaceOnUse">
        <line class="tick" x1="0.4" y1="0" x2="0.4" y2="12"/>
        <line class="tick" x1="3.5" y1="0" x2="3.5" y2="5"/>
        <line class="tick" x1="7" y1="0" x2="7" y2="5"/>
        <line class="tick" x1="10.5" y1="0" x2="10.5" y2="5"/>
        <line class="tick" x1="14" y1="0" x2="14" y2="5"/>
        <line class="tick" x1="17.5" y1="0" x2="17.5" y2="8"/>
        <line class="tick" x1="21" y1="0" x2="21" y2="5"/>
        <line class="tick" x1="24.5" y1="0" x2="24.5" y2="5"/>
        <line class="tick" x1="28" y1="0" x2="28" y2="5"/>
        <line class="tick" x1="31.5" y1="0" x2="31.5" y2="5"/>
      </pattern>
      <pattern id="inch-scale" x="20" y="110" width="90" height="29" patternUnits="userSpaceOnUse">
        <line class="tick" x1="0.4" y1="29" x2="0.4" y2="13"/>
        <line class="tick" x1="11.25" y1="29" x2="11.25" y2="25"/>
        <line class="tick" x1="22.5" y1="29" x2="22.5" y2="22"/>
        <line class="tick" x1="33.75" y1="29" x2="33.75" y2="25"/>
        <line class="tick" x1="45" y1="29" x2="45" y2="19"/>
        <line class="tick" x1="56.25" y1="29" x2="56.25" y2="25"/>
        <line class="tick" x1="67.5" y1="29" x2="67.5" y2="22"/>
        <line class="tick" x1="78.75" y1="29" x2="78.75" y2="25"/>
      </pattern>
    </defs>

    <rect class="ruler-body" x="0" y="0" width="1120" height="139"/>
    <rect class="brand-band" x="0" y="30" width="1120" height="80"/>

    <!-- millimetre scale -->
    <rect x="20" y="0" width="1086" height="30" fill="url(#mm-scale)"/>
    <g class="scale-number" text-anchor="middle">
      <text x="55" y="25">1</text><text x="90" y="25">2</text><text x="125" y="25">3</text>
      <text x="160" y="25">4</text><text x="195" y="25">5</text><text x="230" y="25">6</text>
      <text x="265" y="25">7</text><text x="300" y="25">8</text><text x="335" y="25">9</text>
      <text x="370" y="25">10</text><text x="405" y="25">11</text><text x="440" y="25">12</text>
      <text x="475" y="25">13</text><text x="510" y="25">14</text><text x="545" y="25">15</text>
      <text x="580" y="25">16</text><text x="615" y="25">17</text><text x="650" y="25">18</text>
      <text x="685" y="25">19</text><text x="720" y="25">20</text><text x="755" y="25">21</text>
      <text x="790" y="25">22</text><text x="825" y="25">23</text><text x="860" y="25">24</text>
      <text x="895" y="25">25</text><text x="930" y="25">26</text><text x="965" y="25">27</text>
      <text x="1000" y="25">28</text><text x="1035" y="25">29</text><text x="1070" y="25">30</text>
      <text x="1105" y="25">31</text>
    </g>

    <!-- inch scale -->
    <rect x="20" y="110" width="1081" height="29" fill="url(#inch-scale)"/>
    <g class="scale-number scale-number--inch">
      <text x="114" y="126">1</text><text x="204" y="126">2</text><text x="294" y="126">3</text>
      <text x="384" y="126">4</text><text x="474" y="126">5</text><text x="564" y="126">6</text>
      <text x="654" y="126">7</text><text x="744" y="126">8</text><text x="834" y="126">9</text>
      <text x="924" y="126">10</text><text x="1014" y="126">11</text><text x="1104" y="126">12</text>
    </g>

    <!-- brand name -->
    <g class="brand-lockup">
      <circle class="brand-mark" cx="64" cy="56" r="14"/>
      <text class="brand-name" x="64" y="88" font-size="15" text-anchor="middle">BRODMERE</text>
      <text class="brand-name" x="64" y="101" font-size="8" text-anchor="middle">LIQUID WASTE</text>
    </g>

    <!-- contact details -->
    <g class="contact-list">
      <path class="contact-icon" d="M147 56 q1 -3 3 -2 l1.5 2 q0 1.2 -1 1.6 q1 2.4 3 3.4 q0.6 -1 1.6 -1 l2 1.5 q0.5 2 -2 3 q-7 -1.5 -8.1 -8.5z"/>
      <text class="contact-text" x="164" y="62">08 8317 4925</text>

      <rect class="contact-icon" x="146" y="70" width="11" height="8"/>
      <path class="contact-icon-line" d="M146 70 l5.5 4.5 l5.5 -4.5"/>
      <text class="contact-text" x="164" y="79">info@bwx.com.au</text>

      <circle class="contact-icon" cx="151.5" cy="91" r="5"/>
      <path class="contact-icon-line" d="M146.5 91 h10 M151.5 86 v10 M148.5 87.5 q3 3.5 0 7 M154.5 87.5 q-3 3.5 0 7"/>
      <text class="contact-text" x="164" y="95">www.brodmereliquidwaste.com</text>
    </g>

    <text class="headline" x="1105" y="83" text-anchor="end" textLength="770" lengthAdjust="spacingAndGlyphs">YOUR LOCAL GREASE TRAP AND LIQUID WASTE SPECIALISTS</text>
  </svg>
</div>
</body>
</html>
```